Community coffee table book/quiz book

I need a couple of things for my book:
- Book cover (Title: "1000 gåter om Bakkeskog")
- "Cover pages" for each chapter of the book (15-16 chapters)
- "Watermark" or background design for all the pages of the book.
- A cover image for the book's Facebook page.
- Design of a paper "belt"

The book:
The book will consist of about 200+ pages with ten questions on one page and ten answers on the next.

The name of the book is "1000 gåter om Bakkeskog" which means 1000 questions about Fyllingsdalen (Fyllingsdalen is a suburb of the city Bergen in Norway). Author is Helge Dyrnes.
The questions in the book are grouped in chapters like:
History
Facts
Schools
Businesses
People/profiles
Sport
Culture
Buildings/Landmarks/Sculptures
The different areas of the suburb
The city
Language/expressions
Nature
The names of the chapters are not set, so it would be good to have the option to change the title of the pages without having to contact the designer (maybe by adding the text on top of the cover page?). I therefore suggest that these images are without text.
The book size is 18X18 cm.

The chapter cover pages:
The book will basically consist of text. Ten questions on one page, and ten questions on the next. Visually it will be quite "boring" to look at. I would therefore like to have a chapter cover page for each chapter, preferable in colour.

Water mark:
To avoid having a book full of white pages with limited amount of text I thought of having some kind of design on each page. I do not know how this should be done, but maybe it is possible to create some kind of background image or watermark image with similar design as the book cover and the chapter covers?

The Facebook cover image:
This should be the same as, or similar to, the book cover.
I believe the optimal size is 828px x 315px?

Paper "belt":
The book is to be sold for charity. The receiver of the money is the local sports club. I would like to have the book "wrapped in a 5-6 cm wide paper belt with the logo of the sports club (please see logo and colours here: http://www.ilvarnolia.no). I do not think that the book cover itself should have the sports club's color (purple), but maybe the paper band could? (Again: YOU are the designer)

Photos:
I reckon you would like some photos for both the book cover and the chapter covers. I will of course do the best I can to provide these photos when I have selected a designer. I the meantime

Target Market(s)

Target market is middle clas men and women 35+ from the geographical area Fyllingsdalen.

Industry/Entity Type

Community

Font styles to use
Serif
Sans Serif

Requirements
Must have
• The book will be sold by children on doors. The buyers will probably take a look briefly through the book and then decide if they are going to buy.
• It is important that they like the question types, categories and some of the actual questions they read. But it is also important that they like the look of the book. Therefore the book cover and the chapter cover pages must be appealing enough for the buyers to want this book on theor coffee table.
Nice to have
• I have uploaded a short video clip to Youtube (https://www.klipvista.example/watch?v=qt7Rmx2Lpaw). This a promo clip from Moravel Kids. I felt inspired when I saw it and thought that backgrounds like the ones used in the promo could also be used as backgrounds for each chapter's cover pages. Maybe different colour for each chapter? Screenshots from the clip is uploaded below.
• Then again: Maybe I am an idiot? YOU are the designer :-)
Should not have
• There has been some rivalry between two sportsclubs in the region after the clubs was merged a couple of years ago. I therefore believe we should therefore try avoid both the old clubs' colours (blue&yellow and green) and the new club's colour (purple).

```html
<!DOCTYPE html>
<html lang="en">
<head>
<meta charset="utf-8">
<title>Chapter Cover Pages</title>
<link rel="stylesheet" href="https://fonts.googleapis.com/css2?family=Stardos+Stencil:wght@700&family=Playball&family=Pathway+Gothic+One&display=swap">
<style>
  :root {
    --paper: #ffffff;
    --cover-orange: #f15a24;
    --band-amber: #f7a11a;
    --tape-yellow: #fcb614;
    --tape-light: #fdc83a;
    --block-amber: #f7941d;
    --ink: #1a1a1a;
    --script-white: #ffffff;
  }
  html, body {
    margin: 0;
    padding: 0;
    width: 1200px;
    height: 1000px;
    overflow: hidden;
    background: var(--paper);
  }
  .sheet {
    display: block;
    width: 1200px;
    height: 1000px;
  }
  .cover-field { fill: var(--cover-orange); }
  .cover-band { fill: var(--band-amber); }
  .cover-band-edge { fill: var(--tape-light); opacity: .8; }
  .tape { fill: var(--tape-yellow); opacity: .75; }
  .title-block { fill: var(--block-amber); }
  .title-strip { fill: var(--tape-yellow); opacity: .8; }
  .chapter-title--stencil {
    font-family: "Stardos Stencil", "Arial Black", sans-serif;
    font-weight: 700;
    font-size: 86px;
    fill: var(--ink);
  }
  .chapter-title--script {
    font-family: "Playball", "Georgia", serif;
    font-size: 96px;
    fill: var(--script-white);
  }
  .caption {
    font-family: "Pathway Gothic One", "Arial Narrow", sans-serif;
    font-size: 74px;
    fill: #000;
  }
</style>
</head>
<body>
<svg class="sheet" viewBox="0 0 1200 1000" xmlns="http://www.w3.org/2000/svg">
  <defs>
    <g id="chapter-cover">
      <rect class="cover-field" x="81" y="218" width="490" height="492"/>
      <polygon class="cover-band-edge" points="81,218 571,212 571,220 81,224"/>
      <polygon class="cover-band" points="81,220 571,216 571,262 81,266"/>
      <polygon class="cover-band" points="81,665 571,663 571,708 81,712"/>
      <polygon class="cover-band-edge" points="81,708 571,706 571,711 81,717"/>
      <polygon class="tape" points="441,226 580,258 568,304 431,272"/>
      <polygon class="tape" points="86,625 222,658 212,703 74,671"/>
      <rect class="title-block" x="176" y="340" width="318" height="190"/>
      <polygon class="title-strip" points="169,374 486,343 490,390 172,390"/>
      <polygon class="title-strip" points="172,384 488,388 484,470 178,466"/>
      <polygon class="title-strip" points="183,470 484,466 482,490 186,520"/>
    </g>
  </defs>

  <g class="cover cover--history">
    <use href="#chapter-cover"/>
    <text class="chapter-title--stencil" x="166" y="467" textLength="336" lengthAdjust="spacingAndGlyphs">HISTORY</text>
  </g>

  <g class="cover cover--culture" transform="translate(569 0)">
    <use href="#chapter-cover"/>
    <text class="chapter-title--script" x="161" y="468" textLength="336" lengthAdjust="spacingAndGlyphs">Culture</text>
  </g>

  <text class="caption" x="425" y="805" textLength="333" lengthAdjust="spacingAndGlyphs">COVER PAGES</text>
</svg>
</body>
</html>
```